Flyer-Design für Immobilienmakler
Zielgruppe
Wir sind seit 1992 Immobilienmakler und möchten einen Flyer zur Präsentation unserer Firma und Objektakquise gestalten lassen.
Dieser soll einen Gutschein für eine kostenlose Immobilienbewertung enthalten.
Aufgabenstellung
Wir lassen uns dann überraschen

```html
<!DOCTYPE html>
<html lang="de">
<head>
<meta charset="utf-8">
<title>Luxurious Home – Flyer</title>
<link rel="stylesheet" href="https://fonts.googleapis.com/css2?family=Raleway:wght@300;400;500;600;700&family=Montserrat:wght@700;800&display=swap">
<style>
  :root {
    --yellow: #fdcf61;
    --dark: #2a2a2a;
    --ink: #2b2b2b;
    --muted: #6d6d6d;
    --voucher-grey: #7b7b7b;
    --voucher-red: #d62b2b;
    --faint: #f3f3f3;
    --white: #ffffff;
  }
  * { margin: 0; padding: 0; box-sizing: border-box; }
  html, body { width: 972px; height: 1200px; overflow: hidden; background: var(--white); }
  .flyer {
    position: absolute; left: 0; top: 0;
    width: 1500px; height: 1840px;
    transform: scale(0.648, 0.6522);
    transform-origin: 0 0;
    font-family: "Raleway", sans-serif;
    color: var(--ink);
  }
  .shapes { position: absolute; left: 0; top: 0; width: 1500px; height: 1840px; }
  .abs { position: absolute; }

  .brand { left: 1100px; top: 162px; text-align: right; }
  .brand-tagline { font-size: 25px; font-weight: 500; letter-spacing: 1px; color: var(--dark); }
  .brand-name { font-size: 112px; font-weight: 700; line-height: 0.8; color: var(--dark); letter-spacing: -3px; }

  .headline { right: 57px; top: 555px; text-align: right; }
  .headline h1 { font-size: 62px; font-weight: 700; color: var(--white); line-height: 1.1; }
  .headline h1 .accent { color: var(--yellow); }
  .headline .tag {
    display: inline-block; margin-top: 6px; background: var(--yellow);
    color: var(--dark); font-size: 50px; font-weight: 300; padding: 2px 14px 6px 22px;
  }
  .headline p { margin-top: 20px; color: var(--white); font-size: 20px; line-height: 33px; font-weight: 400; }

  .voucher { left: 884px; top: 890px; width: 569px; height: 292px;
    border-top: 3px solid var(--voucher-red); border-bottom: 3px solid var(--voucher-red); display: flex; }
  .voucher-photo { width: 226px; height: 100%;
    background: linear-gradient(160deg, #eef0f0 0%, #b88a66 45%, #e6e6e6 100%); }
  .voucher-text { flex: 1; background: var(--voucher-grey); color: var(--white);
    font-family: "Montserrat", sans-serif; padding: 12px 18px 0 20px; }
  .voucher-text h2 { font-size: 30px; font-weight: 800; letter-spacing: 2px; margin-bottom: 24px; }
  .voucher-text p { font-size: 19px; font-weight: 700; line-height: 23px; letter-spacing: 0.8px; margin-bottom: 21px; }
  .voucher-text p.light { font-weight: 500; }

  .features { left: 258px; top: 980px; }
  .features h2 { font-size: 50px; font-weight: 700; margin-bottom: 22px; }
  .features ul { list-style: none; display: grid; grid-template-columns: 317px 260px; row-gap: 20px; }
  .features li { font-size: 30px; font-weight: 400; color: #555; line-height: 36px; }
  .features li::before { content: "·"; margin-right: 8px; }

  .about { left: 895px; top: 1252px; width: 548px; }
  .about h2 { font-size: 48px; font-weight: 700; line-height: 60px; }
  .about p.body { margin-top: 24px; font-size: 20px; line-height: 33.5px; color: var(--muted); text-align: justify; }
  .about p.quote { margin-top: 22px; font-size: 21px; line-height: 33px; color: var(--ink); font-weight: 500; }

  .price { left: 894px; top: 1674px; width: 549px; height: 118px; background: var(--yellow); padding: 14px 0 0 50px; }
  .price .label { font-size: 30px; font-weight: 700; }
  .price .amount { font-size: 50px; font-weight: 400; line-height: 56px; }

  .contact { left: 316px; top: 1583px; color: var(--white); font-size: 21px; }
  .contact .row { display: flex; line-height: 40px; }
  .contact .key { width: 74px; font-weight: 700; }
  .contact .address { display: flex; align-items: center; margin-top: 14px; line-height: 33px; }
  .contact .address svg { margin-right: 14px; }
</style>
</head>
<body>
<div class="flyer">
  <svg class="shapes" viewBox="0 0 1500 1840" aria-hidden="false">
    <defs>
      <linearGradient id="houseTones" x1="0" y1="0" x2="0" y2="1">
        <stop offset="0" stop-color="#7fa9d8"/>
        <stop offset="0.35" stop-color="#e9ecee"/>
        <stop offset="0.6" stop-color="#8a8a86"/>
        <stop offset="1" stop-color="#d9d6cf"/>
      </linearGradient>
    </defs>
    <polygon points="620,1525 900,1320 1370,1840 880,1840" fill="var(--faint)"/>
    <polygon points="785,48 1491,48 1491,200 1220,432" fill="var(--yellow)"/>
    <polygon points="1080,330 1220,455 1491,225 1491,1415 1335,1238 884,1238 884,878 1037,878 805,640" fill="var(--dark)"/>
    <polygon points="212,1630 484,1392 880,1840 212,1840" fill="var(--dark)"/>
    <polygon points="212,540 522,922 545,898 212,578" fill="var(--yellow)"/>
    <polygon points="212,48 760,48 1058,315 540,900 212,575" fill="url(#houseTones)" role="img" aria-label="Foto einer modernen weißen Villa mit Glasfront und Pool"/>
  </svg>

  <div class="abs brand">
    <div class="brand-tagline">title goes here</div>
    <div class="brand-name">logo</div>
  </div>

  <div class="abs headline">
    <h1><span class="accent">Luxurious</span> Home</h1>
    <div class="tag">For Rent Or Sale</div>
    <p>Lorem ipsum dolor sit amet, consectetuer<br>adipiscing elit, sed diam nonummy nibh<br>euismod tincidunt ut</p>
  </div>

  <div class="abs voucher">
    <div class="voucher-photo" role="img" aria-label="Foto einer Lupe über einem Hausgrundriss vor einem Wohnhaus"></div>
    <div class="voucher-text">
      <h2>GUTSCHEIN</h2>
      <p>für eine kostenlose<br>Bewertung Ihrer Immobilie.</p>
      <p>Egal ob<br>Haus oder Wohnung</p>
      <p class="light">Wir freuen uns auf Ihren<br>Anruf.</p>
    </div>
  </div>

  <div class="abs features">
    <h2>Property Feature</h2>
    <ul>
      <li>Living Room</li><li>Living Room</li>
      <li>Dining Room</li><li>Dining Room</li>
      <li>3 Bed Room</li><li>3 Bed Room</li>
      <li>Kitchen Room</li><li>Kitchen Room</li>
    </ul>
  </div>

  <div class="abs about">
    <h2>About<br>The Property</h2>
    <p class="body">Lorem ipsum dolor sit amet, consectetuer adipiscing elit, sed diam nonummy nibh euismod tincidunt ut laoreet dolore magna aliquam erat volutpat. Ut wisi enim ad minim veniam, quis nostrud exerci tation ullamcorper suscipit lobortis nisl ut aliquip ex ea commodo consequat.</p>
    <p class="quote">“Ut wisi enim ad minim veniam, quis nostrud exerci tation ullamcorper suscipit lobortis nisl”</p>
  </div>

  <div class="abs price">
    <div class="label">Offering At :</div>
    <div class="amount">$1025000.00</div>
  </div>

  <div class="abs contact">
    <div class="row"><span class="key">Phone</span><span>: 123 456 798 00</span></div>
    <div class="row"><span class="key">E-Mail</span><span>: Your mail address here</span></div>
    <div class="row"><span class="key">Web</span><span>: your website name here</span></div>
    <div class="address">
      <svg width="24" height="34" viewBox="0 0 24 34" aria-hidden="true">
        <path d="M12 0C5.4 0 0 5.3 0 11.9 0 20.5 12 34 12 34s12-13.5 12-22.1C24 5.3 18.6 0 12 0z" fill="#fff"/>
        <circle cx="12" cy="12" r="4.5" fill="var(--dark)"/>
      </svg>
      <div>A9/AB Road Name,<br>City State Area Code-1234</div>
    </div>
  </div>
</div>
</body>
</html>
```